Personal Training Studio needs small flyer design

My Personal Training Studio is looking to offer local high end clothes shops the option to offer their customers free Personal Training at our studio. It will be a small flyer (more a slip - landscape) that can be put into customers shopping bags once they have purchased an item from the store.
It is being marketed as a Local Fitness Initiative which is called "Be Fit In Your Clothes" The idea is to come from a "Be Fit" health perspective but also "Fit into your clothes" from the clothes shops perspective. Perhaps the "Be" in a different colour to the rest of the title. I would like my company logo and colours to be used, plus the address of the of the studio (see website - www.harbourlane7strength.co.uk). Flyer can be double sided

Target Market(s)

High end clothing shops

Industry/Entity Type

Training

Requirements
Must have
• Reference to the fact that the voucher is offering a FREE Personal Training session. Contact us to book yours today.

```html
<!DOCTYPE html>
<html lang="en">
<head>
<meta charset="utf-8">
<title>Be Fit In Your Clothes – Harbourlane7 Strength</title>
<link href="https://fonts.googleapis.com/css2?family=Rubik+Dirt&family=PT+Sans:wght@400;700&family=PT+Sans+Narrow:wght@700&display=swap" rel="stylesheet">
<style>
  :root {
    --page: #e9e7e3;
    --sky-light: #e4f1f8;
    --sky-mid: #b6d6e8;
    --sky-deep: #86b4cf;
    --navy: #2c3f86;
    --ink-navy: #24387a;
    --violet: #5c5f98;
    --teal: #1f5f73;
    --slate: #8d9aa3;
    --band: rgba(160, 170, 178, 0.85);
    --circle-grey: #a3a7ab;
    --white: #ffffff;
    --skin: #c99a7d;
    --gym-grey: #9aa6ad;
  }
  * { box-sizing: border-box; margin: 0; padding: 0; }
  html, body { width: 1200px; height: 1000px; overflow: hidden; background: var(--page); }
  body { position: relative; font-family: "PT Sans", sans-serif; }

  .flyer {
    position: absolute; left: 100px; top: 205px; width: 1000px; height: 590px;
    overflow: hidden;
    background: linear-gradient(135deg, var(--sky-mid) 0%, var(--sky-light) 45%, var(--sky-mid) 75%, var(--sky-deep) 100%);
    box-shadow: 0 10px 30px rgba(0,0,0,0.18);
  }
  .facets { position: absolute; inset: 0; }

  .photo-lifter {
    position: absolute; left: 0; top: 300px; width: 400px; height: 290px;
    background: radial-gradient(ellipse at 55% 55%, var(--skin) 0%, #b48d78 35%, var(--gym-grey) 70%, #c7d3da 100%);
  }
  .photo-trainer {
    position: absolute; right: 0; top: 0; width: 280px; height: 235px;
    background: linear-gradient(180deg, #d9c1b0 0%, var(--skin) 45%, #9ea3a8 100%);
  }
  .corner-disc {
    position: absolute; left: 660px; top: -110px; width: 200px; height: 200px;
    border-radius: 50%; background: var(--violet);
  }
  .grey-disc {
    position: absolute; left: 610px; top: 70px; width: 130px; height: 130px;
    border-radius: 50%; background: var(--circle-grey);
  }

  .headline { position: absolute; left: 0; top: 0; width: 1000px; height: 330px; font-family: "Rubik Dirt", sans-serif; font-weight: 400; }
  .headline .be { position: absolute; left: 100px; top: 120px; font-size: 140px; line-height: 1; color: var(--navy); }
  .headline .fit-in, .headline .clothes { position: absolute; color: var(--white); white-space: nowrap; line-height: 1;
    text-shadow: 3px 3px 0 rgba(30,40,70,0.55); }
  .headline .fit-in { left: 330px; top: 140px; font-size: 66px; }
  .headline .clothes { left: 250px; top: 240px; font-size: 58px; letter-spacing: -1px; }

  .offer { position: absolute; left: 540px; top: 332px; width: 280px; }
  .offer-free { background: var(--teal); color: var(--white); height: 74px; display: flex; align-items: flex-end; padding: 0 10px 6px; gap: 8px; }
  .offer-free strong { font-family: "PT Sans Narrow", sans-serif; font-size: 72px; line-height: 1; }
  .offer-free span { font-size: 28px; line-height: 1.4; }
  .offer-where { background: var(--slate); color: var(--white); font-size: 25px; padding: 2px 10px 4px; white-space: nowrap; }

  .brand { position: absolute; left: 820px; top: 300px; width: 180px; height: 140px; background: var(--navy);
    display: flex; align-items: center; justify-content: center; gap: 8px; padding: 0 10px; }
  .brand-dot { width: 10px; height: 10px; background: var(--white); flex: none; }
  .brand-name { color: var(--white); font-size: 17px; font-weight: 700; line-height: 1.15; }

  .contact { position: absolute; left: 0; top: 440px; width: 1000px; height: 150px; background: var(--band);
    padding: 14px 0 0 310px; color: var(--ink-navy); }
  .contact .phones { font-size: 44px; line-height: 1.05; }
  .contact .address { font-size: 23px; color: var(--white); margin-top: 4px; }
  .contact .web { font-size: 38px; font-weight: 700; line-height: 1.15; }
</style>
</head>
<body>
  <main class="flyer">
    <svg class="facets" width="1000" height="590" aria-hidden="true">
      <polygon points="300,0 520,0 420,180" fill="#ffffff" opacity="0.18"/>
      <polygon points="420,180 620,260 520,430" fill="#ffffff" opacity="0.14"/>
      <polygon points="520,0 700,0 620,160" fill="#7fb0cc" opacity="0.18"/>
      <polygon points="420,180 520,430 330,400" fill="#7fb0cc" opacity="0.15"/>
    </svg>
    <div class="corner-disc"></div>
    <div class="grey-disc"></div>
    <div class="photo-trainer" role="img" aria-label="Photo of a trainer holding a towel over his shoulder"></div>
    <div class="photo-lifter" role="img" aria-label="Photo of a man lifting a dumbbell in the gym"></div>

    <h1 class="headline">
      <span class="be">Be</span>
      <span class="fit-in">Fit In</span>
      <span class="clothes">Your Clothes</span>
    </h1>

    <div class="offer">
      <div class="offer-free"><strong>FREE</strong><span>Personal</span></div>
      <div class="offer-where">Training at our studio</div>
    </div>

    <div class="brand">
      <span class="brand-dot"></span>
      <span class="brand-name">HARBOURLANE7<br>STRENGTH</span>
    </div>

    <footer class="contact">
      <p class="phones">07700 900312 • 01632 960418</p>
      <p class="address">7 Harbour Lane, Kelby, North Yorkshire KB2 4LQ</p>
      <p class="web">harbourlane7strength.co.uk</p>
    </footer>
  </main>
</body>
</html>
```